Web Design Front Page Only for Organic Skincare

We have been in business for nearly 20 years. We are run by all females and sell anything from aromatherapy, skincare and pharmacy types products to health food shops and pharmacy. We are looking for an attractive and colourful but simple front web page design for our wholesale customers to look at. We want our customers to start using our website to find information rather than ringing us. So we want it to be attractive to our buyers who are young and funky.
Updates

To give you an idea of the products we sell to pharmacy and health food shops also beauty shops and hair salons.  We mainly deal with organic body and skincare, aromatherapy oils and body products, but also do some simple pharmacy products such as bandages and pill boxes, finger splits, walking frames and wheelchairs.  We are only looking for the front page of the website.  The back-end will be done in-house.  We currently do not have a logo designed so I am thinking that once we have done the website design we can build a logo from it.  I like bright colours and want something that is inviting to further discover that we do many different types of products.

Target Market(s)

young girls who are our retail buyers

Industry/Entity Type

Pharmacy

Requirements
Must have
• A section which says

Customer Log in
Should not have
• don't worry about too much writing or tabs. We will insert these later. Just come up with design image.

```html
<!DOCTYPE html>
<html lang="en">
<head>
<meta charset="utf-8">
<title>Petal &amp; Root – Skin Care</title>
<link href="https://fonts.googleapis.com/css2?family=Arvo:wght@400;700&family=PT+Sans:wght@400;700&family=Yanone+Kaffeesatz:wght@400&display=swap" rel="stylesheet">
<style>
:root{
  --dark:#262626;
  --pink:#e52a5a;
  --blush:#f8eaf0;
  --plum:#5c1660;
  --plum-2:#8a1a78;
  --wine:#a3102f;
  --gold:#e9c26b;
  --white:#ffffff;
}
*{margin:0;padding:0;box-sizing:border-box}
html,body{width:970px;height:1200px;overflow:hidden}
body{position:relative;background:var(--blush);font-family:"PT Sans",Arial,sans-serif;color:var(--plum)}
.abs{position:absolute}

/* header */
.header{left:0;top:0;width:970px;height:488px;background:radial-gradient(ellipse at 48% 0%,#4a4a4a 0%,var(--dark) 55%,#1e1e1e 100%)}
.brand{left:155px;top:28px;display:flex;align-items:center;gap:10px}
.brand-mark{width:14px;height:14px;border-radius:50%;background:var(--white)}
.brand-name{font-size:26px;color:var(--white);font-weight:400;letter-spacing:.5px}
.brand-tag{left:190px;top:70px;width:228px;border-top:1px solid #aaa;padding-top:6px;text-align:center;font-size:10px;letter-spacing:3px;color:#ddd}
.login{left:592px;top:82px;font-size:11px;font-weight:700;letter-spacing:.5px;color:#f7a0b8}
.quote-tag{left:728px;top:4px;width:100px;height:100px}
.quote-text{left:740px;top:32px;width:80px;text-align:center;line-height:1.1}
.quote-text .small{font-size:14px;color:#5e8a70;font-weight:700}
.quote-text .mid{font-size:10px;color:var(--wine)}
.quote-text .big{font-size:19px;color:var(--wine);font-weight:700}

/* nav */
.nav{left:113px;top:113px;width:762px;height:43px}
.nav-item{top:121px;font-family:"Yanone Kaffeesatz","Arial Narrow",sans-serif;font-size:18px;color:var(--white);line-height:26px;white-space:nowrap}
.search{left:712px;top:125px;width:115px;height:21px;background:var(--white);border-radius:3px;font-size:13px;color:#aaa;padding:1px 5px}
.search svg{position:absolute;right:4px;top:5px}

/* hero */
.hero{left:149px;top:182px;width:666px;height:278px;border-radius:12px;overflow:hidden;background:linear-gradient(100deg,#f6ece6 0%,#eed2c3 35%,#d9a890 60%,#f3e5df 85%,#ffffff 100%)}
.hero-vines-l{left:88px;top:165px;width:70px;height:320px;background:linear-gradient(180deg,rgba(90,150,120,0),rgba(90,150,120,.35),rgba(90,150,120,0))}
.hero-vines-r{left:810px;top:165px;width:70px;height:320px;background:linear-gradient(180deg,rgba(90,150,120,0),rgba(90,150,120,.35),rgba(90,150,120,0))}
.hero-copy{left:169px;top:310px;font-family:Arvo,Georgia,serif;font-size:16.5px;line-height:21px;color:var(--wine);white-space:nowrap;text-shadow:0 0 4px #fff}
.ribbon{left:690px;top:175px;width:135px;height:135px}
.dots{left:722px;top:468px;display:flex;gap:9px}
.dots span{width:10px;height:10px;border-radius:50%;background:var(--pink)}
.dots span.on{background:#f5a8bd;box-shadow:0 0 0 2px var(--pink)}

/* content */
.intro{left:143px;top:499px;width:178px;font-size:10px;line-height:11px;color:var(--plum)}
.intro span{display:block;text-align:justify;text-align-last:justify}
.intro span.last{text-align-last:left}
.topics{left:143px;top:580px;list-style:none}
.topics li{font-size:9px;font-weight:700;letter-spacing:.9px;color:var(--plum);height:18.2px;padding-left:12px;position:relative}
.topics li::before{content:"";position:absolute;left:1px;top:2px;border-left:5px solid var(--plum);border-top:4px solid transparent;border-bottom:4px solid transparent}
.new-title{left:141px;top:751px;font-size:12px;font-weight:400;color:var(--plum-2)}
.product{left:141px;top:774px;width:156px;height:100px;background:var(--white)}
.product-img{left:173px;top:780px;width:92px;height:88px;border-radius:40%;background:linear-gradient(180deg,#e7e0d0,#3d93c9 55%,#2b6ea5)}
.arrow{top:802px;width:0;height:0;border-top:20px solid transparent;border-bottom:20px solid transparent}
.arrow.l{left:143px;border-right:7px solid #bbb}
.arrow.r{left:289px;border-left:7px solid #bbb}
.divider{left:333px;top:494px;width:1px;height:432px;background:#e3c6d2}

.article{left:360px;top:505px;width:473px;font-size:8.8px;line-height:10.9px;color:var(--plum);text-align:justify;letter-spacing:.1px}
.article h2{font-size:8.8px;font-weight:400;margin-bottom:11px}
.article p{margin-bottom:11px}

/* reviews */
.reviews-bg{left:0;top:940px;width:970px;height:160px;background:linear-gradient(180deg,var(--blush) 0%,#f0d5df 60%,#ecd0da 100%)}
.reviews-title{left:134px;top:929px;font-family:Arvo,Georgia,serif;font-size:14.5px;font-weight:700;color:var(--plum-2)}
.card{top:958px;width:169px;height:102px;background:var(--white);border:1px solid #d8b9c6;padding:3px;box-shadow:0 1px 3px rgba(0,0,0,.15)}
.card .pic{width:100%;height:100%}
.card .label{position:absolute;right:8px;bottom:4px;font-family:Arvo,Georgia,serif;font-size:12.5px;font-weight:700;color:var(--plum-2)}
.c1{left:134px}.c1 .pic{background:linear-gradient(90deg,#f4eee8,#e9d3c4 50%,#f6f2ee)}
.c2{left:314px}.c2 .pic{background:linear-gradient(120deg,#e7c3a8,#cfd77a 50%,#f0e8e4)}
.c3{left:493px}.c3 .pic{background:linear-gradient(90deg,#e6c09c,#f4dcc4 55%,#fbf6f2)}
.c4{left:672px}.c4 .pic{background:linear-gradient(120deg,#f6d6dc,#ee8fa2 45%,#f4ece6)}

/* footer */
.footer{left:0;top:1100px;width:970px;height:100px;background:var(--dark)}
.footer-rule{left:0;top:1104px;width:970px;border-top:1px dashed #bbb}
.f-brand{left:138px;top:1124px;display:flex;align-items:center;gap:8px}
.f-brand .brand-mark{width:11px;height:11px}
.f-brand .brand-name{font-size:20px}
.f-tag{left:160px;top:1155px;width:185px;border-top:1px solid #aaa;padding-top:4px;text-align:center;font-size:8px;letter-spacing:2.5px;color:#ddd}
.f-links{left:360px;top:1146px;font-size:7.6px;color:#bbb;letter-spacing:.2px;white-space:pre}
.copy{left:437px;top:1178px;font-size:7.6px;color:#aaa}
.social{top:1118px;width:19px;height:19px;border-radius:3px}
.s1{left:758px;background:#3b6fb8}
.s2{left:786px;background:#e8e8e8}
.s3{left:814px;background:#5fb4e0}
</style>
</head>
<body>

<header class="abs header"></header>

<div class="abs brand"><span class="brand-mark"></span><span class="brand-name">Petal &amp; Root</span></div>
<div class="abs brand-tag">20 Years in Market</div>
<a class="abs login">Customer Log in</a>

<svg class="abs quote-tag" viewBox="0 0 100 100" aria-hidden="true">
  <path d="M22 6 L78 6 Q90 6 92 18 L96 80 Q96 96 80 98 L22 98 Q6 96 6 80 L8 18 Q10 6 22 6Z" fill="#f8e6c8" transform="rotate(-6 50 50)"/>
  <circle cx="58" cy="14" r="4" fill="#5a4a3a"/>
</svg>
<div class="abs quote-text"><div class="small">Request</div><div class="mid">A</div><div class="big">Quote</div></div>

<svg class="abs nav" viewBox="0 0 762 43" aria-hidden="true">
  <polygon points="0,0 762,0 742,21.5 762,43 0,43 20,21.5" fill="#e52a5a"/>
  <line x1="22" y1="4" x2="740" y2="4" stroke="#f7a0b8" stroke-dasharray="3 3"/>
  <line x1="22" y1="39" x2="740" y2="39" stroke="#f7a0b8" stroke-dasharray="3 3"/>
</svg>
<nav>
  <span class="abs nav-item" style="left:153px">Home</span>
  <span class="abs nav-item" style="left:202px">Beauty Products</span>
  <span class="abs nav-item" style="left:311px">Cosmetic</span>
  <span class="abs nav-item" style="left:386px">Nutrition Product</span>
  <span class="abs nav-item" style="left:507px">Skincare Product</span>
  <span class="abs nav-item" style="left:624px">Heath care</span>
</nav>
<div class="abs search">search
  <svg width="10" height="10" viewBox="0 0 10 10"><circle cx="4" cy="4" r="3" fill="none" stroke="#999" stroke-width="1.4"/><line x1="6.2" y1="6.2" x2="9" y2="9" stroke="#999" stroke-width="1.4"/></svg>
</div>

<div class="abs hero-vines-l" role="img" aria-label="Climbing green vine with leaves"></div>
<div class="abs hero-vines-r" role="img" aria-label="Climbing green vine with leaves"></div>
<div class="abs hero" role="img" aria-label="Close-up beauty photograph with a rose in the lower corner"></div>
<p class="abs hero-copy">Skin care &nbsp;provides<br>information, articles and tips on<br>how to keep your skin look<br>healthy, beautiful and glowing, as<br>beautiful skin is what makes your<br>first impression.</p>
<svg class="abs ribbon" viewBox="0 0 135 135" aria-hidden="true">
  <polygon points="22,0 56,0 135,79 135,113" fill="#e9c26b"/>
  <text x="0" y="0" transform="translate(57,12) rotate(45)" font-family="Arvo, Georgia, serif" font-size="12" font-weight="700" fill="#3a2a10">100% Naturel</text>
</svg>
<div class="abs dots"><span class="on"></span><span></span><span></span><span></span></div>

<p class="abs intro"><span>Skin troubles and diseases are</span><span>emerging with more reasons behind</span><span>them, most of the skin issues being</span><span>wrinkles, rashes, skin infection and</span><span>allergy, paleness or darkening of skin</span><span class="last">and many more.</span></p>
<ul class="abs topics">
  <li>Permanent hair removal</li>
  <li>Facial skin problems</li>
  <li>Wrinkles and pores</li>
  <li>Skin diseases</li>
  <li>Skin Disorders</li>
  <li>Skin rash</li>
  <li>Mini Face Lift</li>
  <li>Causes of Eczema</li>
</ul>
<h3 class="abs new-title">New Products</h3>
<div class="abs product"></div>
<div class="abs product-img" role="img" aria-label="Jar of organic body butter"></div>
<div class="abs arrow l"></div><div class="abs arrow r"></div>
<div class="abs divider"></div>

<article class="abs article">
  <h2>Skin Care Fundamentals</h2>
  <p>A lot of people are besieged by all the ads that say their skin care product will make their skin look a lot better over-night. And this is just normal in these days of excessive media hype over skin products. However, the good thing is that skincare tips are not that complicated. Keeping the face clean need not have to be a huge procedure, and there is no need to shell out too much on skin products. All you have to do is give your skin the right care.</p>
  <h2>Cleansers</h2>
  <p>Most people know the importance of cleansing in skin care. The main idea behind using a cleanser is to clear up dirt and excess oils from the skin. The sad part is that there are some cleansers that can badly affect the skin. And there are people who get dry skin just due to their cleansers, and not because of any natural dryness. These folks never realize that the wrong type of cleanser can actually hurt the skin. First of all you need to know the various alternatives for cleansers. Bar type soaps are the most extreme cleansers however they are also the best for clearing up dirt. Liquid cleansers arrive in various types and tolerability and are fine for all skin types except the oily ones. A facial cleanser is the mildest type but they may not get rid of dirt and oil as well. The bottom-line is that you need not aim for complete dryness for the sake of cleanliness. You can just go for a gentle cleanser that never-theless takes away all the dirt.</p>
  <h2>Moisturizers</h2>
  <p>Moisturizing is very important for proper skin care. By using the right Moisturizer you can prevent the dryness from escalating further into cracked and flaky skin. A successful moisturizer will be one that has a good mix of constituents that refill the natural ingredients of the skin that help uphold its structure. A few ingredients normally found in an up to date moisturizer include Glycerol, Ceramides, Hydroxy Acids and Niacinamide. Glycerol facilitates water along with other moisturizer elements to go through the skin and get to the places required. Ceramides replenishes oils in the skin. Hydroxy Acids facilitates exfoliation of skin cells that are dead. Niacinamide makes the skin to increase production of oils, and may possibly assist in reversing the marks of sun damage. Just like how skin types are different, the moisturizers also vary in their action and constituents. So it is important that you pick the right one from the skin care reviews for a beautiful glowing skin.</p>
  <h2>Sunscreen</h2>
  <p>Regrettably, there is a lot of sun damage happening under the surface of the skin due to UV radiation, without anyone noticing it until it gets too severe. It is a familiar fact that contact to UV rays can cause sunburn, skin damage and augmentation of skin cancer risk. However people fail to note that this problem also happens when they are not directly under the sun. Even small amounts of exposure can add up in the long run and cause dark spots, wrinkles, and even cancer of the skin. There is no use of working hard for skin care and finally ruining it with sun exposure. So the smart thing to do is to get a good sunscreen and use it regularly. Pedi care and manicure helps in giving your legs and hands a good look leaving your fingers and skin soft and glowing soon after a hot sunny day.</p>
</article>

<div class="abs reviews-bg" role="img" aria-label="Soft pink diamond pattern"></div>
<h3 class="abs reviews-title">Product Reviews</h3>
<div class="abs card c1"><div class="pic" role="img" aria-label="Spa treatment with white lily"></div><span class="label">Beauty Products</span></div>
<div class="abs card c2"><div class="pic" role="img" aria-label="Hand holding a jar of cream"></div><span class="label">Cosmetic Products</span></div>
<div class="abs card c3"><div class="pic" role="img" aria-label="Smiling woman with green apple"></div><span class="label">Womens Health</span></div>
<div class="abs card c4"><div class="pic" role="img" aria-label="Pink carnation with soap bar"></div><span class="label">Nutrition Product</span></div>

<footer class="abs footer"></footer>
<div class="abs footer-rule"></div>
<div class="abs f-brand"><span class="brand-mark"></span><span class="brand-name">Petal &amp; Root</span></div>
<div class="abs f-tag">20 Years in Market</div>
<div class="abs f-links">HOME  |  PRIVACY POLICY  |  DISCLAIMER  |  SITE MAP  |   COPYRIGHTS  |   CONTACT US</div>
<div class="abs copy">© Copyright 2012 company name</div>
<div class="abs social s1"></div>
<svg class="abs social s2" viewBox="0 0 19 19" aria-label="Email"><rect width="19" height="19" rx="3" fill="#e8e8e8"/><rect x="3" y="5" width="13" height="9" fill="#fff" stroke="#999"/><polyline points="3,5 9.5,10.5 16,5" fill="none" stroke="#999"/></svg>
<div class="abs social s3"></div>

</body>
</html>
```